Information Technology Company needs a Website...

We need a single page website for new technology company called:

MERIDEL FALLS TECHNOLOGY GROUP
Based in Ojai CA.

We are offering three primary services:

- Business Solutions

- IT Services

- Software Implementation and Consulting

We want a single page design where all content scrolls down/up on one page. We're looking for the following characteristics:

- Home/Landing
- Active background with panoramic view (Will provide content)

- Business Solutions, IT Services, Software Implementation and Consulting

List of software vendors we recommend (Company logos)

- About
- History
- Our Team
- Partners

I'll upload our new logo as soon as we get the design files. I'll also send over some example website layout's that we like shortly.

Target Market(s)

Small/Medium Businesses

Industry/Entity Type

Information Technology

Number of Pages Required

1 page

Font styles to use
Other font styles liked:
• Sansation

Requirements
Must have
• Full page browser width, easy navigation and visibility. Creative design, not like every other "Technology" website template. Should be the "One Page" design where each section is below the next and the user scrolls down the page through the whole site. I like the concept of the following website in the main "Whiteboard" image:
• http://www.plavorix.com/design/4829137
• And the way this site does the active panoramic background:
• http://www.kelbrantworks.com/
• Something interesting and appealing to potential clients looking for Small/Medium business solutions and IT Services.
• Use uploaded Logo to establish color and theme for website.
Should not have
• Look the same as every other information technology website template.

```html
<!DOCTYPE html>
<html lang="en">
<head>
<meta charset="utf-8">
<title>Meridel Falls Technology Group</title>
<link rel="stylesheet" href="https://fonts.googleapis.com/css2?family=Play:wght@400;700&family=Arimo:wght@400;700&display=swap">
<style>
  :root {
    --orange: #f05a28;
    --orange-deep: #e04e22;
    --ink: #444444;
    --body-text: #777777;
    --light-panel: #efefef;
    --white: #ffffff;
    --hero-dark: #2b2d31;
    --footer-bg: #4a4a4a;
    --heading-font: "Play", sans-serif;
    --body-font: "Arimo", sans-serif;
  }
  * { box-sizing: border-box; margin: 0; padding: 0; }
  html, body { width: 1200px; height: 2456px; overflow: hidden; }
  body { position: relative; background: var(--white); font-family: var(--body-font); color: var(--body-text); }

  /* Hero */
  .hero { position: absolute; left: 0; top: 0; width: 1200px; height: 680px; overflow: hidden; }
  .hero-backdrop { position: absolute; inset: 0; background: radial-gradient(ellipse at 50% 40%, #5a5e66 0%, #3a3d43 45%, var(--hero-dark) 100%); }
  .hero-cut { position: absolute; left: 0; bottom: 0; width: 1200px; height: 145px; }
  .main-nav { position: absolute; top: 15px; left: 0; width: 1200px; height: 52px; }
  .main-nav a { position: absolute; top: 0; height: 52px; line-height: 52px; color: var(--white); text-decoration: none; font-family: var(--heading-font); font-size: 18px; text-transform: uppercase; }
  .main-nav a.is-active { background: var(--orange); padding: 0 23px; }
  .brand { position: absolute; top: 228px; left: 0; width: 1200px; text-align: center; color: var(--white); font-family: var(--heading-font); font-weight: 700; }
  .brand-name { display: block; font-size: 64px; line-height: 70px; letter-spacing: -1px; text-transform: lowercase; }
  .brand-sub { display: block; font-size: 23px; line-height: 34px; letter-spacing: 5px; margin-top: 6px; }
  .brand-mark { display: block; width: 22px; height: 22px; border: 3px solid var(--white); border-radius: 50%; margin: 0 auto 14px; }

  /* Shared headings */
  .section-title { font-family: var(--heading-font); font-weight: 400; font-size: 40px; color: var(--ink); text-transform: uppercase; }
  .section-title span { color: var(--orange); }
  .lead { font-size: 15px; line-height: 27px; color: var(--body-text); }

  /* Welcome */
  .welcome { position: absolute; top: 645px; left: 0; width: 1200px; text-align: center; }
  .welcome .lead { width: 830px; margin: 18px auto 0; }
  .partner-row { position: absolute; top: 205px; left: 0; width: 1200px; height: 44px; }
  .partner { position: absolute; top: 0; height: 44px; line-height: 44px; font-family: var(--heading-font); font-weight: 700; font-size: 26px; color: #222222; display: flex; align-items: center; gap: 10px; }
  .partner i { display: inline-block; width: 24px; height: 24px; background: #222222; }
  .partner i.round { border-radius: 50%; }

  /* History */
  .history { position: absolute; top: 953px; left: 0; width: 1200px; height: 399px; background: var(--light-panel); }
  .history-visual { position: absolute; left: 0; top: 0; width: 600px; height: 399px; background: radial-gradient(circle at 50% 40%, #6b6e73 0%, #303236 55%, #1a1b1e 100%); }
  .history-copy { position: absolute; left: 628px; top: 36px; width: 500px; }
  .history-copy .lead { margin-top: 14px; }
  .history-copy .lead + .lead { margin-top: 6px; }

  /* Services */
  .services { position: absolute; top: 1352px; left: 0; width: 1200px; height: 542px; text-align: center; }
  .services > .section-title { margin-top: 60px; }
  .services > .lead { width: 850px; margin: 14px auto 0; }
  .service { position: absolute; top: 198px; width: 340px; text-align: center; }
  .service-icon { width: 124px; height: 124px; border-radius: 50%; background: #f0f0f0; margin: 0 auto; display: flex; align-items: center; justify-content: center; }
  .service-title { margin-top: 24px; height: 56px; font-family: var(--heading-font); font-size: 20px; line-height: 26px; color: var(--orange); text-transform: uppercase; font-weight: 400; }
  .service .lead { width: 260px; margin: 22px auto 0; }

  /* Team */
  .team { position: absolute; top: 1894px; left: 0; width: 1200px; height: 447px; background: linear-gradient(135deg, #f0653a 0%, var(--orange-deep) 100%); text-align: center; }
  .team-notch { position: absolute; top: 0; left: 564px; }
  .team .section-title { position: absolute; top: 92px; left: 0; width: 1200px; color: #222222; }
  .member { position: absolute; top: 182px; width: 220px; text-align: center; color: var(--white); }
  .member-photo { width: 144px; height: 144px; border-radius: 50%; border: 3px solid var(--white); background: linear-gradient(160deg, #d9d9d9, #8f8f8f); margin: 0 auto; }
  .member-name { margin-top: 18px; font-family: var(--heading-font); font-size: 20px; font-weight: 400; }
  .member-site { font-size: 15px; margin-top: 2px; }

  /* Footer */
  .site-footer { position: absolute; top: 2341px; left: 0; width: 1200px; height: 115px; background: var(--footer-bg); color: var(--white); }
  .footer-nav { position: absolute; left: 79px; top: 32px; display: flex; gap: 0; }
  .footer-nav a { color: var(--white); text-decoration: none; font-size: 14px; margin-right: 24px; }
  .copyright { position: absolute; left: 79px; top: 66px; font-size: 14px; }
  .copyright span { color: var(--orange); }
  .social { position: absolute; left: 953px; top: 33px; display: flex; gap: 9px; }
  .social span { width: 36px; height: 36px; border-radius: 50%; border: 2px solid var(--white); }
  .social span.is-filled { background: var(--orange); border-color: var(--orange); }
</style>
</head>
<body>

<header class="hero">
  <div class="hero-backdrop" role="img" aria-label="Businessman in a suit behind translucent charts and a stock graph"></div>
  <svg class="hero-cut" width="1200" height="145" viewBox="0 0 1200 145" aria-hidden="true">
    <polygon points="0,145 0,140 600,2 1200,140 1200,145" fill="#ffffff"/>
  </svg>
  <nav class="main-nav">
    <a class="is-active" href="#home" style="left:155px">Home</a>
    <a href="#about" style="left:293px">About Us</a>
    <a href="#history" style="left:424px">History</a>
    <a href="#services" style="left:540px">Services</a>
    <a href="#team" style="left:665px">Our Team</a>
    <a href="#partners" style="left:802px">Partners</a>
    <a href="#contact" style="left:936px">Contact Us</a>
  </nav>
  <div class="brand">
    <span class="brand-mark"></span>
    <span class="brand-name">meridel falls</span>
    <span class="brand-sub">TECHNOLOGY GROUP</span>
  </div>
</header>

<section class="welcome" id="about">
  <h1 class="section-title">Welcome to <span>Meridel Falls</span></h1>
  <p class="lead">Lorem Ipsum is simply dummy text of the printing and typesetting industry. Lorem Ipsum has been the industry's standard dummy text ever since the 1500s, when an unknown printer took a galley of type and scrambled it to make a type specimen book. It has survived not only five centuries, but also the leap into electronic typesetting, remaining essentially unchanged. It was popularised in the 1960s with the release of Letraset sheets</p>
  <div class="partner-row" id="partners">
    <div class="partner" style="left:218px;font-size:20px"><i></i>Corvantis</div>
    <div class="partner" style="left:380px;font-size:22px"><i class="round"></i>Hollenby</div>
    <div class="partner" style="left:576px"><i></i>Brastow</div>
    <div class="partner" style="left:828px"><i></i>Quenlar</div>
  </div>
</section>

<section class="history" id="history">
  <div class="history-visual" role="img" aria-label="Hand touching a glowing network of connected nodes"></div>
  <div class="history-copy">
    <h2 class="section-title">Our <span>History</span></h2>
    <p class="lead">Lorem Ipsum is simply dummy text of the printing and typesetting industry. Lorem Ipsum has been the industry's standard dummy text ever since the 1500s, when an unknown printer took a galley of type and scrambled it to make a type specimen book.</p>
    <p class="lead">It has survived not only five centuries, but also the leap into electronic typesetting, remaining essentially unchanged. It was popularised in the 1960s with the release of Letraset sheets.</p>
    <p class="lead">Lorem Ipsum has been the industry's standard dummy text ever since the 1500s, when an unknown printer took.</p>
  </div>
</section>

<section class="services" id="services">
  <h2 class="section-title">Our <span>Services</span></h2>
  <p class="lead">Lorem Ipsum is simply dummy text of the printing and typesetting industry. Lorem Ipsum has been the industry's standard dummy text ever since the 1500s, when an unknown printer took.</p>

  <div class="service" style="left:71px">
    <div class="service-icon">
      <svg width="64" height="64" viewBox="0 0 64 64" aria-hidden="true" fill="none" stroke="#f05a28" stroke-width="4" stroke-linecap="round">
        <path d="M32 16a13 13 0 0 0-8 23v6h16v-6a13 13 0 0 0-8-23z" fill="#f05a28"/>
        <line x1="26" y1="51" x2="38" y2="51"/>
        <line x1="32" y1="4" x2="32" y2="9"/><line x1="12" y1="12" x2="16" y2="16"/><line x1="52" y1="12" x2="48" y2="16"/>
        <line x1="4" y1="30" x2="9" y2="30"/><line x1="55" y1="30" x2="60" y2="30"/>
      </svg>
    </div>
    <h3 class="service-title">Business Solutions</h3>
    <p class="lead">Lorem Ipsum is simply dummy text of the printing and typesetting industry. Lorem Ipsum ext ever since the..</p>
  </div>

  <div class="service" style="left:430px">
    <div class="service-icon">
      <svg width="64" height="64" viewBox="0 0 64 64" aria-hidden="true" fill="none" stroke="#f05a28" stroke-width="3.5" stroke-linecap="round">
        <path d="M18 38a10 10 0 0 1 2-20 14 14 0 0 1 26 2 9 9 0 0 1 0 18z"/>
        <line x1="24" y1="30" x2="24" y2="52"/><line x1="32" y1="26" x2="32" y2="56"/><line x1="40" y1="30" x2="40" y2="52"/>
        <circle cx="24" cy="55" r="3" fill="#f05a28"/><circle cx="32" cy="58" r="3" fill="#f05a28"/><circle cx="40" cy="55" r="3" fill="#f05a28"/>
      </svg>
    </div>
    <h3 class="service-title">IT Services</h3>
    <p class="lead">Lorem Ipsum is simply dummy text of the printing and typesetting industry. Lorem Ipsum ext ever since the..</p>
  </div>

  <div class="service" style="left:796px">
    <div class="service-icon">
      <svg width="72" height="64" viewBox="0 0 72 64" aria-hidden="true">
        <polyline points="6,34 24,18 34,26 60,6" fill="none" stroke="#f05a28" stroke-width="3.5" stroke-linecap="round"/>
        <polygon points="52,4 64,2 62,14" fill="#f05a28"/>
        <circle cx="24" cy="38" r="7" fill="#f05a28"/><circle cx="48" cy="38" r="7" fill="#f05a28"/><circle cx="36" cy="34" r="8" fill="#f05a28"/>
        <path d="M12 60a12 12 0 0 1 24 0z M36 60a12 12 0 0 1 24 0z M22 60a14 14 0 0 1 28 0z" fill="#f05a28"/>
      </svg>
    </div>
    <h3 class="service-title">Software Implementation &amp; Consulting</h3>
    <p class="lead">Lorem Ipsum is simply dummy text of the printing and typesetting industry. Lorem Ipsum ext ever since the..</p>
  </div>
</section>

<section class="team" id="team" role="img" aria-label="Orange tinted backdrop of business icons and a hand on a tablet">
  <svg class="team-notch" width="72" height="34" viewBox="0 0 72 34" aria-hidden="true">
    <polygon points="0,0 72,0 36,34" fill="#ffffff"/>
  </svg>
  <h2 class="section-title">Our Teeam</h2>
  <div class="member" style="left:91px">
    <div class="member-photo" role="img" aria-label="Portrait of a team member"></div>
    <p class="member-name">Member Name</p><p class="member-site">something.com</p>
  </div>
  <div class="member" style="left:357px">
    <div class="member-photo" role="img" aria-label="Portrait of a team member"></div>
    <p class="member-name">Member Name</p><p class="member-site">something.com</p>
  </div>
  <div class="member" style="left:625px">
    <div class="member-photo" role="img" aria-label="Portrait of a team member"></div>
    <p class="member-name">Member Name</p><p class="member-site">something.com</p>
  </div>
  <div class="member" style="left:889px">
    <div class="member-photo" role="img" aria-label="Portrait of a team member"></div>
    <p class="member-name">Member Name</p><p class="member-site">something.com</p>
  </div>
</section>

<footer class="site-footer" id="contact">
  <nav class="footer-nav">
    <a href="#home">Home</a><a href="#about">About Us</a><a href="#history">History</a><a href="#services">Services</a><a href="#team">Our team</a><a href="#partners">partner</a><a href="#contact">Contact Us</a>
  </nav>
  <p class="copyright">©<span>Meridel Falls technology group</span> - 2016 All rights reserved.</p>
  <div class="social" aria-label="Social links">
    <span class="is-filled"></span><span></span><span></span><span></span>
  </div>
</footer>

</body>
</html>
```